Valto Sàrl - Business Card

VALTO Sàrl operates in the sector Services for banks and credit institutions. It is a B2B which connects companies. The main colors should be Blue and Black. The logo and look of the card should be simple, professional, conservative and reflect Connecting People.

Target Market(s)

Financial professionals and institutions

Industry/Entity Type

Finance

Contact Information for Business Card

Chemin des Prés 9
1027 Lonay

Logo Text

Connecting dots

Font styles to use
Serif
Sans Serif

Colors
0355a3
3176b5
85acd3
cfdeed

Requirements
Should not have
• Multiple colors

```html
<!DOCTYPE html>
<html lang="fr">
<head>
<meta charset="utf-8">
<title>Valto Sàrl – Business Card</title>
<link rel="stylesheet" href="https://fonts.googleapis.com/css2?family=Montserrat:wght@600;700&family=Arimo:wght@400&display=swap">
<style>
  :root {
    --blue-deep: #0355a3;
    --blue-mid: #3176b5;
    --blue-soft: #85acd3;
    --blue-pale: #cfdeed;
    --ink: #2b2b2b;
    --paper: #ffffff;
    --backdrop: #e9edf2;
  }
  * { margin: 0; padding: 0; box-sizing: border-box; }
  html, body { width: 1189px; height: 1200px; overflow: hidden; }
  body { background: var(--backdrop); position: relative; font-family: "Arimo", Arial, sans-serif; }

  .card {
    position: absolute; left: 169px; width: 851px; height: 484px;
    border-radius: 38px; overflow: hidden;
  }
  .card--front { top: 112px; background: var(--paper); box-shadow: 0 4px 14px rgba(0,0,0,.12); }
  .card--back { top: 642px; background: var(--blue-deep); box-shadow: 0 4px 14px rgba(0,0,0,.18); }

  .brand { position: absolute; display: flex; flex-direction: column; align-items: center; }
  .brand__dot { border-radius: 50%; }
  .brand__name { font-family: "Montserrat", Arial, sans-serif; font-weight: 700; white-space: nowrap; line-height: 1; }

  .card--front .brand { left: 70px; top: 140px; width: 320px; }
  .card--front .brand__dot { width: 120px; height: 120px; background: var(--blue-mid); margin-bottom: 30px; }
  .card--front .brand__name { font-size: 50px; color: var(--blue-deep); }

  .divider { position: absolute; left: 425px; top: 134px; width: 2px; height: 216px; background: var(--blue-soft); }

  .contact { position: absolute; left: 486px; top: 128px; color: var(--ink); }
  .contact__name { font-family: "Montserrat", Arial, sans-serif; font-weight: 700; font-size: 29px; color: var(--blue-deep); line-height: 1.1; }
  .contact__role { font-size: 21px; margin-top: 2px; }
  .contact__address { font-size: 20px; line-height: 27px; margin-top: 20px; }
  .contact__list { list-style: none; margin-top: 16px; }
  .contact__item { display: flex; align-items: center; font-size: 20px; height: 31px; }
  .contact__icon { width: 22px; height: 22px; margin-right: 14px; flex: none; }

  .back-field { position: absolute; inset: 0; background: radial-gradient(circle at 50% 45%, var(--blue-deep) 0%, #1f63ab 70%, var(--blue-deep) 100%); }
  .card--back .brand { left: 0; width: 100%; top: 160px; }
  .card--back .brand__dot { width: 110px; height: 110px; background: var(--blue-soft); margin-bottom: 40px; }
  .card--back .brand__name { font-size: 54px; color: var(--paper); }
</style>
</head>
<body>
  <section class="card card--front">
    <div class="brand">
      <span class="brand__dot"></span>
      <span class="brand__name">Valto Sàrl</span>
    </div>
    <div class="divider"></div>
    <div class="contact">
      <p class="contact__name">Lena Moret</p>
      <p class="contact__role">Manager</p>
      <p class="contact__address">Chemin des Prés 9<br>1027 Lonay</p>
      <ul class="contact__list">
        <li class="contact__item">
          <svg class="contact__icon" viewBox="0 0 24 24"><circle cx="12" cy="12" r="12" fill="var(--blue-deep)"/><path d="M8.5 6.5l2 0 1 3-1.4 1.1a7 7 0 0 0 3.3 3.3l1.1-1.4 3 1v2a1.5 1.5 0 0 1-1.6 1.5A10 10 0 0 1 7 8.1 1.5 1.5 0 0 1 8.5 6.5z" fill="#fff"/></svg>
          (021) 555 0148
        </li>
        <li class="contact__item">
          <svg class="contact__icon" viewBox="0 0 24 24"><circle cx="12" cy="12" r="12" fill="var(--blue-deep)"/><rect x="6" y="8" width="12" height="8.5" rx="1" fill="none" stroke="#fff" stroke-width="1.4"/><path d="M6.3 8.5l5.7 4.3 5.7-4.3" fill="none" stroke="#fff" stroke-width="1.4"/></svg>
          contact@valtosarl.ch
        </li>
        <li class="contact__item">
          <svg class="contact__icon" viewBox="0 0 24 24"><circle cx="12" cy="12" r="12" fill="var(--blue-deep)"/><g fill="none" stroke="#fff" stroke-width="1.2"><circle cx="12" cy="12" r="6.5"/><ellipse cx="12" cy="12" rx="3" ry="6.5"/><path d="M5.5 12h13M6.5 8.8h11M6.5 15.2h11"/></g></svg>
          www.valtosarl.ch
        </li>
      </ul>
    </div>
  </section>

  <section class="card card--back">
    <div class="back-field" role="img" aria-label="Large faint brand pattern in blue tones"></div>
    <div class="brand">
      <span class="brand__dot"></span>
      <span class="brand__name">Valto Sàrl</span>
    </div>
  </section>
</body>
</html>
```